Quorbly Resource Book - 10 maths tasks to do outside

I need a 22 (11 pages back to back) page A6 sized book produced to standard for submission to professional printer. Needs to be as .pdf file showing guide lines and allowances for colour bleed. I have text already written and submitted as attachment in a Word file with margins set to A6 size. The theme of the materials is "Brisk Yard" so using lots of pictures from nature (Australia preferably) and showing lots of patterns in nature (rocks, leaves, flower petals etc). Some of the tasks refer to specific activities, such as "shadows" and "floating" so would be great to illustrate appropriately. The big emphasis is on learning outside the classroom, getting kids to engage actively with nature. I would like to see the pages as full colour - so not white background. The book itself will be spiral bound along the top edge so a margin of at least 1cm will be required at the top of each page (or the bottom of even numbered pages). Book will be printed on plastic laminated matte paper for outdoor use. Font size needs to be big enough to read. Fonts sizes, alignments and page numbers are all different at the moment and need to be standardised. One photo is included in a page as a sample if you can use it, otherwise disregard. Logo for Harlow Vale Learning Association is also included to have as part of the acknowledgements at the back of the book.

Book is for early childhood and preschool teachers.

Education

Sans Serif

• Colour and appeal.
• Use of natural colours instead of bright catchy colours but that is your call.
• American spelling

```html
<!DOCTYPE html>
<html lang="en">
<head>
<meta charset="utf-8">
<title>Thanks – Quorbly Resource Book</title>
<link rel="stylesheet" href="https://fonts.googleapis.com/css2?family=Jost:wght@400;500;800&display=swap">
<style>
  :root {
    --paper: #ffffff;
    --crop: #9a9a9a;
    --sky-top: #c9a7a5;
    --sky-glow: #f2b070;
    --sky-haze: #a79da6;
    --water-mid: #7d7378;
    --water-deep: #4f4a52;
    --ink: #2e2b2e;
    --title: #263a8f;
    --title-edge: #ffffff;
  }
  html, body {
    margin: 0;
    padding: 0;
    overflow: hidden;
    background: var(--paper);
  }
  .canvas {
    position: relative;
    width: 892px;
    height: 1200px;
    background: var(--paper);
    overflow: hidden;
    font-family: "Jost", sans-serif;
  }
  .crop-marks {
    position: absolute;
    inset: 0;
  }
  .page {
    position: absolute;
    left: 53px;
    top: 53px;
    width: 786px;
    height: 1094px;
    overflow: hidden;
  }
  .page-backdrop {
    position: absolute;
    inset: 0;
    background:
      radial-gradient(ellipse 55% 22% at 42% 34%, rgba(250, 200, 120, 0.85), rgba(250, 200, 120, 0) 70%),
      linear-gradient(180deg,
        var(--sky-top) 0%,
        var(--sky-glow) 18%,
        var(--sky-haze) 32%,
        #8f8688 40%,
        #d8a070 44%,
        var(--water-mid) 55%,
        #625b62 72%,
        var(--water-deep) 100%);
  }
  .page-content {
    position: absolute;
    left: 72px;
    top: 50px;
    width: 641px;
    color: var(--ink);
  }
  .title {
    margin: 0 0 22px;
    text-align: center;
    font-weight: 800;
    font-size: 50px;
    line-height: 1.1;
    letter-spacing: -0.5px;
    color: var(--title);
    -webkit-text-stroke: 5px var(--title-edge);
    paint-order: stroke fill;
  }
  .body-text {
    margin: 0 0 12px;
    font-size: 29px;
    font-weight: 400;
    line-height: 44px;
    text-align: justify;
    text-indent: 29px;
  }
</style>
</head>
<body>
<div class="canvas">
  <svg class="crop-marks" width="892" height="1200" viewBox="0 0 892 1200" aria-hidden="true">
    <g stroke="var(--crop)" stroke-width="1" fill="none">
      <path d="M53 0V43M0 53H43M75 0V75H53M53 75V53"/>
      <path d="M839 0V43M892 53H849M817 0V75H839"/>
      <path d="M53 1200V1157M0 1147H43M75 1200V1125H53"/>
      <path d="M839 1200V1157M892 1147H849M817 1200V1125H839"/>
      <path d="M0 75H53M892 75H839M0 1125H53M892 1125H839"/>
    </g>
  </svg>

  <section class="page">
    <div class="page-backdrop" role="img" aria-label="Photograph of a lake at sunset, with trees on the left shore, distant hills and rippled water reflecting an orange sky"></div>
    <div class="page-content">
      <h1 class="title">Thanks</h1>
      <p class="body-text">I would like to acknowledge the Ngunnawal people, the tradition custodians of the land and carers for the magnificent environment in which Canberra is located and through which we are engaging in this project.</p>
      <p class="body-text">I would like to acknowledge the support of the Tarrin Shire Council Brisk Yard Grant Program and the Harlow Vale Learning Association in the production of this resource.</p>
      <p class="body-text">I would also like to thank the following people who contributed to the ideas and development of the resource:</p>
      <p class="body-text">Nadia Corwell, Rochelle Fenwick, Emmeline Grady, Alec Hollister, Jenna Lockwood, Tessa Lorne, Molly Quinlan, Judith Ransome, Marion Rowbury, Leigh Wexford, Alana Whitcombe, Sian Welbeck</p>
      <p class="body-text">Original artwork by Perry Tallmont, Grey Heron Studio</p>
    </div>
  </section>
</div>
</body>
</html>
```